Page to pitch my newly published book. See www.TalesBeneathTheCopperBridge.com.

Need some pics to set the stage, maybe a skyline of Philadelphia, a pic of my book, etc. Began setting up a page but it is not public and has only my profile pic. Waiting for a high resolution pic of the book.

```html
<!DOCTYPE html>
<html lang="en">
<head>
<meta charset="utf-8">
<title>Tales Beneath the Copper Bridge – Page</title>
<link href="https://fonts.googleapis.com/css2?family=Roboto:wght@400;500;700&family=Roboto+Condensed:ital,wght@0,300;0,400;1,700&family=Source+Sans+3:ital,wght@0,400;0,600;0,700;1,700&display=swap" rel="stylesheet">
<style>
:root{
  --bar:#3b5998;
  --page:#e9ebee;
  --card:#ffffff;
  --line:#dddfe2;
  --text:#1d2129;
  --muted:#90949c;
  --link:#365899;
  --action:#4b4f56;
  --cta:#4080ff;
  --tile:#5b8be6;
  --green:#14863f;
  --dark:#262626;
  --sand1:#e6dcc6;
  --sand2:#c9b997;
  --create:#42b72a;
}
*{box-sizing:border-box;margin:0;padding:0}
html,body{width:900px;height:1200px;overflow:hidden}
body{background:var(--page);font-family:"Roboto",Arial,sans-serif;color:var(--text);position:relative;font-size:9px}
.abs{position:absolute}
.topbar{left:0;top:0;width:900px;height:29px;background:var(--bar)}
.topbar .mark{left:99px;top:6px;width:17px;height:17px;background:#fff;border-radius:2px}
.topbar .search{left:122px;top:6px;width:296px;height:15px;background:#fff;border-radius:2px}
.topbar .search svg{position:absolute;right:8px;top:3px}
.topbar .user{left:550px;top:6px;display:flex;align-items:center;gap:6px;color:#fff;font-weight:700;font-size:8.5px}
.topbar .avatar-sm{width:14px;height:16px;background:#8a7a6c}
.topbar .home{left:624px;top:9px;color:#fff;font-weight:700;font-size:8.5px}
.topbar .icons{left:666px;top:7px;display:flex;gap:8px}

.profile-pic{left:101px;top:37px;width:111px;height:111px;background:#fff;border:1px solid var(--line);padding:3px}
.profile-pic div{width:100%;height:100%;background:linear-gradient(180deg,#1b9447,#117a38)}
.page-name{left:99px;top:157px;font-size:17px;display:flex;align-items:center;gap:5px}
.verified{width:14px;height:14px;border-radius:50%;background:var(--cta)}

.side-nav{left:99px;top:219px;width:117px}
.side-nav a{display:block;height:21.4px;line-height:21.4px;padding-left:7px;color:#4b4f56;font-size:9.5px;text-decoration:none}
.side-nav a.active{background:#dcdee3;border-left:2px solid var(--bar);color:var(--text);font-weight:700;height:20px;line-height:20px}
.create{left:104px;top:380px;width:67px;height:15px;background:var(--create);color:#fff;font-size:7.5px;font-weight:500;text-align:center;line-height:15px;border-radius:2px}

.cover{left:222px;top:30px;width:552px;height:208px;background:linear-gradient(90deg,var(--sand2),var(--sand1) 55%,#ddd2b9)}
.cover .art{left:18px;top:8px;width:332px;height:192px;background:linear-gradient(100deg,#6b6f5a,#2f7a44 35%,#a69a80 60%,#7c6e5c)}
.cover-title{left:348px;top:22px;font-family:"Source Sans 3",Arial,sans-serif;color:#1f1f1f}
.cover-title .a{font-size:20px;font-weight:600;line-height:20px}
.cover-title .b{font-size:33px;font-weight:700;font-style:italic;line-height:34px}
.cover-title .c{font-size:16px;font-weight:600;line-height:20px}
.cover-title .d{font-size:15px;font-weight:400;line-height:20px}
.cover-title .e{font-size:10.5px;font-weight:700;margin-top:10px}
.cover-tag{right:18px;top:173px;width:300px;text-align:right;font-family:"Roboto Condensed",Arial,sans-serif;font-size:8px;font-weight:700;line-height:10px;color:#222}

.actions-bar{left:222px;top:238px;width:552px;height:35px;background:var(--card);border:1px solid var(--line);border-top:0}
.btn-group{left:9px;top:9px;display:flex;border:1px solid #ced0d4;border-radius:2px;background:#f6f7f9}
.btn-group span{padding:0 8px;height:16px;line-height:16px;font-size:8px;font-weight:700;color:#4b4f56;border-right:1px solid #ced0d4}
.btn-group span:last-child{border-right:0}
.btn-group .liked{color:var(--link)}
.contact{left:344px;top:8px;width:199px;height:19px;background:var(--cta);color:#fff;font-size:9.5px;text-align:center;line-height:19px}

.card{background:var(--card);border:1px solid var(--line);border-radius:2px}
.composer{left:222px;top:282px;width:335px;height:71px}
.composer .tabs{height:22px;background:#f6f7f9;border-bottom:1px solid var(--line);display:flex;align-items:center;gap:6px;padding-left:12px;font-size:8px;color:#4b4f56}
.composer .tabs .lnk{color:var(--link)}
.face{background:linear-gradient(180deg,#9b8c7c,#5d5048)}
.composer .face{left:9px;top:30px;width:27px;height:27px}
.composer .ph{left:44px;top:39px;color:var(--muted);font-size:9.5px}

.post-head .face-page{width:25px;height:26px;background:var(--green);border:1px solid var(--line)}
.post-head{left:8px;top:8px;display:flex;gap:7px}
.post-head .who{font-size:7.5px;color:var(--muted);line-height:11px}
.post-head .who b{font-weight:400;color:var(--link);font-size:9.5px}
.post-head .who em{font-style:normal;color:var(--link)}
.post-head .who .ch{color:#4b4f56}
.chev{right:10px;top:10px}
.post-acts{display:flex;gap:22px;font-size:8px;color:var(--action);padding-left:12px}
.post-acts span{display:flex;align-items:center;gap:5px}
.react{display:flex;align-items:center;gap:4px;font-size:8px;color:var(--link)}
.dots{display:flex}
.dots i{width:10px;height:10px;border-radius:50%;margin-right:-2px;border:1px solid #fff}
.top-c{font-size:8px;color:var(--link)}
.cbox{height:22px;border:1px solid var(--line);border-radius:2px;background:#fff;color:var(--muted);font-size:9px;line-height:20px;padding-left:9px}
.foot{background:#f6f7f9;border-top:1px solid var(--line)}

.post1{left:222px;top:362px;width:335px;height:264px}
.post1 .pic{left:8px;top:45px;width:320px;height:123px;background:linear-gradient(90deg,#9b8e74,#d9cdb3)}
.post1 .pic .art{left:10px;top:4px;width:176px;height:115px;background:linear-gradient(100deg,#5f6553,#2f7a44 35%,#a69a80 62%,#7c6e5c)}
.mini-title{left:202px;top:16px;font-family:"Source Sans 3",Arial,sans-serif;color:#1f1f1f;line-height:1}
.mini-title .a{font-size:10px;font-weight:600}
.mini-title .b{font-size:17px;font-weight:700;font-style:italic;margin:1px 0}
.mini-title .c{font-size:8px;font-weight:600}
.mini-title .d{font-size:8px;margin-top:2px}
.mini-title .e{font-size:5.5px;font-weight:700;margin-top:6px}
.mini-tag{right:12px;top:102px;text-align:right;font-family:"Roboto Condensed",Arial,sans-serif;font-size:4.5px;font-weight:700;line-height:6px}

.post2{left:222px;top:634px;width:335px;height:528px}
.post2 .body-text{left:8px;top:51px;width:310px;font-size:8px;line-height:11px}
.promo{left:7px;top:81px;width:321px;height:321px;background:var(--dark)}
.promo .greenside{left:0;top:0;width:113px;height:321px;background:var(--green)}
.promo .book{left:17px;top:26px;width:142px;height:202px;background:linear-gradient(180deg,#1f9a4c,#128240);box-shadow:0 2px 4px rgba(0,0,0,.4)}
.promo .copy{left:173px;top:38px;width:136px;font-family:"Roboto Condensed",Arial,sans-serif;font-weight:300;color:#eeeeee;font-size:8px;line-height:11.2px;text-align:justify}
.promo .copy .lead{font-style:italic;font-weight:700;margin-bottom:9px;text-align:left}
.promo .copy p+p{margin-top:10px}
.promo .urlbar{left:113px;top:286px;width:208px;height:20px;background:var(--green);color:#fff;font-family:"Roboto Condensed",Arial,sans-serif;font-style:italic;font-weight:700;font-size:10.5px;line-height:20px;padding-left:4px}

.rcol{left:565px;width:209px}
.r-site{top:282px;height:28px;padding:9px 8px;font-size:9.5px}
.r-search{top:318px;height:26px;padding:8px 8px;font-size:9px;color:var(--muted);display:flex;gap:8px;align-items:center}
.r-likes{top:352px;height:66px}
.r-likes .face{left:8px;top:4px;width:20px;height:24px}
.r-likes .n{left:35px;top:5px;font-size:8.5px;line-height:13px}
.r-likes .n span{color:var(--muted)}
.r-likes .inv{left:0;top:34px;width:100%;border-top:1px solid var(--line);padding:10px 0 0 35px;font-size:7.8px}
.r-head{height:22px;border-bottom:1px solid var(--line);padding:0 8px;font-size:7.5px;font-weight:500;color:#4b4f56;display:flex;justify-content:space-between;align-items:center}
.r-about{top:428px;height:92px}
.r-about .row{display:flex;gap:6px;padding:0 8px;font-size:8px;line-height:11.5px;color:#333}
.r-about .row i{width:6px;height:6px;border-radius:50%;border:1px solid #bbb;margin-top:3px;flex:none}
.r-photos{top:530px;height:214px}
.tile{position:absolute;background:var(--tile)}
.r-videos{top:756px;height:190px}
.vid{position:absolute;background:linear-gradient(180deg,var(--tile) 60%,#2d5bb8)}
.vstat{position:absolute;bottom:4px;color:#fff;font-size:8px;display:flex;gap:10px}
</style>
</head>
<body>

<header class="topbar abs">
  <div class="mark abs" aria-label="Site mark"></div>
  <div class="search abs">
    <svg width="9" height="9" viewBox="0 0 9 9"><circle cx="3.7" cy="3.7" r="2.8" fill="none" stroke="#666" stroke-width="1"/><line x1="5.8" y1="5.8" x2="8.5" y2="8.5" stroke="#666"/></svg>
  </div>
  <div class="user abs"><div class="avatar-sm" role="img" aria-label="Profile photo of the visitor"></div>John Smith</div>
  <div class="home abs">Home</div>
  <div class="icons abs">
    <svg width="14" height="12" viewBox="0 0 14 12"><circle cx="4" cy="3" r="2.5" fill="#fff"/><circle cx="10" cy="3" r="2.5" fill="#dbe3f3"/><path d="M0 12c0-4 8-4 8 0z" fill="#fff"/><path d="M6 12c0-4 8-4 8 0z" fill="#dbe3f3"/></svg>
    <svg width="13" height="12" viewBox="0 0 13 12"><rect x="0" y="1" width="10" height="7" rx="1" fill="#fff"/><path d="M2 8v3l3-3z" fill="#fff"/><rect x="5" y="3" width="8" height="6" rx="1" fill="#dbe3f3"/></svg>
    <svg width="12" height="12" viewBox="0 0 12 12"><circle cx="6" cy="6" r="5.5" fill="#fff"/><path d="M3 4l2 1 0 3 2 1M8 2l1 3 2 0" stroke="#3b5998" fill="none"/></svg>
    <svg width="24" height="12" viewBox="0 0 24 12"><rect x="0" y="2" width="10" height="8" fill="#dbe3f3"/><path d="M15 5l3 3 3-3z" fill="#dbe3f3"/></svg>
  </div>
</header>

<div class="profile-pic abs"><div role="img" aria-label="Green book cover of Tales Beneath the Copper Bridge with a vintage photo of a boy"></div></div>
<div class="page-name abs">Vellowick.com <span class="verified"><svg width="14" height="14" viewBox="0 0 14 14"><path d="M4 7l2 2 4-4" stroke="#fff" stroke-width="1.6" fill="none"/></svg></span></div>

<nav class="side-nav abs">
  <a class="active" href="#">Home</a>
  <a href="#">Photos</a>
  <a href="#">Likes</a>
  <a href="#">About</a>
  <a href="#">Videos</a>
  <a href="#">Welcome</a>
  <a href="#">Posts</a>
</nav>
<div class="create abs">Create a Page</div>

<section class="cover abs">
  <div class="art abs" role="img" aria-label="Hardcover book mockup beside a vintage photograph of a young boy seated on wooden steps"></div>
  <div class="cover-title abs">
    <div class="a">Tales</div>
    <div class="b">Beneath</div>
    <div class="c">the Copper Bridge</div>
    <div class="d">- Marion Delacroix Hale</div>
    <div class="e">www.talesbeneaththecopperbridge.com</div>
  </div>
  <div class="cover-tag abs">Read the story of Walter J. Hale, a humble and unassuming man,<br>who lived with dignity, faith, and humor.</div>
</section>

<div class="actions-bar abs">
  <div class="btn-group abs"><span class="liked">&#128077; Liked ▾</span><span>Message</span><span>··· More ▾</span></div>
  <div class="contact abs">Contact Us</div>
</div>

<section class="composer card abs">
  <div class="tabs"><span>✎ Status</span><span class="lnk">▣ Photo / Video</span></div>
  <div class="face abs" role="img" aria-label="Visitor profile photo"></div>
  <div class="ph abs">Write something on this Page...</div>
</section>

<article class="post1 card abs">
  <div class="post-head abs">
    <div class="face-page" role="img" aria-label="Page profile photo"></div>
    <div class="who"><b>www.vellowick.com/route/</b> <span class="ch">changed their</span> <em>cover photo.</em><br>2 mins · ◍</div>
  </div>
  <svg class="chev abs" width="8" height="5" viewBox="0 0 8 5"><path d="M0 0l4 4 4-4" stroke="#aaa" fill="none"/></svg>
  <div class="pic abs">
    <div class="art abs" role="img" aria-label="Book mockup and vintage photograph of a young boy"></div>
    <div class="mini-title abs"><div class="a">Tales</div><div class="b">Beneath</div><div class="c">the Copper Bridge</div><div class="d">- Marion Delacroix Hale</div><div class="e">www.talesbeneaththecopperbridge.com</div></div>
    <div class="mini-tag abs">Read the story of Walter J. Hale, a humble and unassuming man,<br>who lived with dignity, faith, and humor.</div>
  </div>
  <div class="abs" style="left:0;top:178px;width:100%;height:20px;border-top:1px solid var(--line);padding-top:5px">
    <div class="post-acts"><span>&#128077; Like</span><span>▭ Comment</span><span>➦ Share</span></div>
    <div class="face abs" style="right:10px;top:4px;width:13px;height:13px" role="img" aria-label="Visitor photo"></div>
  </div>
  <div class="foot abs" style="left:0;top:200px;width:100%;height:63px">
    <div class="react abs" style="left:8px;top:8px"><span class="dots"><i style="background:#4080ff"></i><i style="background:#f33e58"></i><i style="background:#f7b125"></i></span>1.6M</div>
    <div class="top-c abs" style="right:8px;top:8px">Top Comments ▾</div>
    <div class="face abs" style="left:8px;top:33px;width:21px;height:21px" role="img" aria-label="Visitor photo"></div>
    <div class="cbox abs" style="left:37px;top:33px;width:290px">Write a comment...</div>
  </div>
</article>

<article class="post2 card abs">
  <div class="post-head abs">
    <div class="face-page" role="img" aria-label="Page profile photo"></div>
    <div class="who"><b>www.vellowick.com/route/</b> <span class="ch">changed their</span> <em>cover photo.</em><br>June 17 · ◍</div>
  </div>
  <svg class="chev abs" width="8" height="5" viewBox="0 0 8 5"><path d="M0 0l4 4 4-4" stroke="#aaa" fill="none"/></svg>
  <p class="body-text abs">Lorem ipsum dolor sit amet timeti ergo sum Lorem ipsum dolor sit amet timeti dolor sit amet timeti imeti ergo sum imeti ergo sum</p>
  <div class="promo abs">
    <div class="greenside abs"></div>
    <div class="book abs" role="img" aria-label="Book cover of Tales Beneath the Copper Bridge by Marion Delacroix Hale, with a framed vintage photo of a boy"></div>
    <div class="copy abs">
      <div class="lead">Tales Beneath the Copper Bridge is a biography of my father, Walter J. Hale.</div>
      <p>It traces his humble beginnings as a child of Irish immigrants in Chestnut Hill Pennsylvania to many far away countries, where he fought valiantly for his country. But that was not the beginning nor the end of his story.</p>
      <p>Walt drew on courage and faith throughout his lifetime and he learned from a very young age how important prayer was, and never stopped praying. He and my mother began their married life in Denver, CO after the war and raised eleven children. Walt showed great courage during the war and drew on that same courage after the war to overcome the scars he carried from his time in combat.</p>
    </div>
    <div class="urlbar abs">www.TalesBeneathTheCopperBridge.com</div>
  </div>
  <div class="abs" style="left:0;top:412px;width:100%;height:20px;border-top:1px solid var(--line);padding-top:7px">
    <div class="post-acts"><span>&#128077; Like</span><span>▭ Comment</span><span>➦ Share</span></div>
    <div class="face abs" style="right:10px;top:5px;width:13px;height:13px" role="img" aria-label="Visitor photo"></div>
  </div>
  <div class="foot abs" style="left:0;top:436px;width:100%;height:91px">
    <div class="react abs" style="left:8px;top:10px"><span class="dots"><i style="background:#4080ff"></i><i style="background:#f33e58"></i><i style="background:#f7b125"></i></span>1.6M</div>
    <div class="top-c abs" style="right:8px;top:12px">Top Comments ▾</div>
    <div class="abs" style="left:8px;top:38px;font-size:8px;color:var(--link)">11,397 shares</div>
    <div class="abs" style="right:8px;top:38px;font-size:8px;color:var(--muted)">15K Comments</div>
    <div class="face abs" style="left:8px;top:62px;width:21px;height:21px" role="img" aria-label="Visitor photo"></div>
    <div class="cbox abs" style="left:34px;top:62px;width:293px">Write a comment...</div>
  </div>
</article>

<aside>
  <div class="rcol card abs r-site">Personal Website</div>
  <div class="rcol card abs r-search"><svg width="9" height="9" viewBox="0 0 9 9"><circle cx="3.7" cy="3.7" r="2.8" fill="none" stroke="#888"/><line x1="5.8" y1="5.8" x2="8.5" y2="8.5" stroke="#888"/></svg>Search for Posts on the Page</div>
  <div class="rcol card abs r-likes">
    <div class="face abs" role="img" aria-label="Friend profile photo"></div>
    <div class="n abs">1,955,550 people like this<br><span>Tom Smith and 20 other friends</span></div>
    <div class="inv abs"><svg class="abs" style="left:12px;top:9px" width="12" height="10" viewBox="0 0 12 10"><circle cx="4" cy="3" r="2.5" fill="#bec3c9"/><path d="M0 10c0-4 8-4 8 0z" fill="#bec3c9"/><path d="M10 2v4M8 4h4" stroke="#bec3c9"/></svg>Invite friends to like this Page</div>
  </div>
  <div class="rcol card abs r-about">
    <div class="r-head">ABOUT <span>›</span></div>
    <div class="row" style="margin-top:10px"><i></i><span>Lorem ipsum dolor sit amet timeti ergo sum Lorem ipsum dolor sit amet timeti dolor sit amet timeti imeti ergo sum imeti ergo sum</span></div>
    <div class="row" style="margin-top:8px;color:var(--link)"><i></i><span>http://www.vellowick.com/</span></div>
  </div>
  <div class="rcol card abs r-photos">
    <div class="r-head">PHOTOS <span>›</span></div>
    <div class="tile" style="left:5px;top:24px;width:65px;height:60px"></div>
    <div class="tile" style="left:74px;top:24px;width:65px;height:60px"></div>
    <div class="tile" style="left:142px;top:24px;width:64px;height:60px"></div>
    <div class="tile" style="left:5px;top:87px;width:65px;height:60px"></div>
    <div class="tile" style="left:74px;top:87px;width:65px;height:60px"></div>
    <div class="tile" style="left:142px;top:87px;width:64px;height:60px"></div>
    <div class="tile" style="left:5px;top:150px;width:65px;height:60px"></div>
    <div class="tile" style="left:74px;top:150px;width:65px;height:60px"></div>
    <div class="tile" style="left:142px;top:150px;width:64px;height:60px"></div>
  </div>
  <div class="rcol card abs r-videos">
    <div class="r-head">VIDEOS <span>›</span></div>
    <div class="vid" style="left:5px;top:24px;width:200px;height:98px">
      <svg class="abs" style="left:73px;top:22px" width="56" height="56" viewBox="0 0 56 56"><circle cx="28" cy="28" r="26" fill="none" stroke="#fff" stroke-width="2.5"/><path d="M22 17l17 11-17 11z" fill="#fff"/></svg>
      <div class="vstat" style="right:10px">&#128077; 139K <span>▭ 2.2K</span></div>
    </div>
    <div class="vid" style="left:5px;top:126px;width:98px;height:60px"><div class="vstat" style="left:6px">&#128077; 139K <span style="margin-left:14px">▭ 2.2K</span></div></div>
    <div class="vid" style="left:108px;top:126px;width:97px;height:60px"><div class="vstat" style="left:6px">&#128077; 139K <span style="margin-left:14px">▭ 2.2K</span></div></div>
  </div>
</aside>

</body>
</html>
```